TR & Groundworks
Landscaping
TR & Groundworks - Utilities
Creative Brief
Professional
Dennis Holloway
Brisk Meadow Cooling and Yardcraft LLP
P.O. Box 618207 Christiansted, St. Croix 00822
Briskmeadowcoolingandyardcraft@mailvessel.com
Mona Fairweather is the Co-Owner name needs to be on card also

```html
<!DOCTYPE html>
<html lang="en">
<head>
<meta charset="utf-8">
<title>Brisk Meadow Business Card</title>
<link href="https://fonts.googleapis.com/css2?family=Arimo:wght@400;700&display=swap" rel="stylesheet">
<style>
  :root {
    --page: #ffffff;
    --front-pale: #f4f8ee;
    --front-green: #c9e2ae;
    --band-light: #bcd9f3;
    --band-mid: #7fb3e3;
    --band-dark: #3f87c9;
    --navy: #10284a;
    --ink: #1d2a36;
    --brand-green: #1f7a2c;
    --back-top: #2f7ccd;
    --back-bottom: #e9f3fc;
    --shadow: rgba(0, 0, 0, 0.28);
  }
  * { margin: 0; padding: 0; box-sizing: border-box; }
  html, body {
    width: 1200px; height: 422px; overflow: hidden;
    background: var(--page);
    font-family: "Arimo", Arial, sans-serif;
  }
  .canvas { position: relative; width: 1200px; height: 422px; }

  .card {
    position: absolute; top: 43px;
    width: 554px; height: 341px;
    box-shadow: 2px 3px 6px var(--shadow);
    overflow: hidden;
  }

  /* Front */
  .card-front {
    left: 19px;
    background: linear-gradient(135deg, var(--front-green) 0%, var(--front-pale) 45%, #ffffff 100%);
  }
  .name-band {
    position: absolute; left: 0; right: 0; top: 111px; height: 70px;
    background: linear-gradient(90deg, var(--band-dark) 0%, var(--band-mid) 35%, var(--band-light) 100%);
    border-top: 2px solid #ffffff; border-bottom: 2px solid #ffffff;
  }
  .names {
    position: absolute; left: 278px; top: 117px;
    color: var(--navy);
    font-weight: 700; font-size: 24px; line-height: 30px;
    letter-spacing: 0.5px; text-transform: uppercase;
    white-space: nowrap;
  }
  .front-brand {
    position: absolute; left: 18px; top: 22px; width: 200px;
  }
  .front-brand .brand-dot {
    display: block; width: 42px; height: 42px; border-radius: 50%;
    background: var(--brand-green); margin: 0 0 6px 58px;
  }
  .front-brand .brand-name {
    font-weight: 700; font-size: 44px; line-height: 48px;
    color: var(--brand-green); text-align: center;
  }
  .front-brand .brand-tagline {
    font-weight: 700; font-size: 9px; letter-spacing: 0.5px;
    color: var(--brand-green); text-transform: uppercase;
    text-align: center; margin-top: 4px; white-space: nowrap;
  }
  .contact {
    position: absolute; right: 26px; bottom: 26px;
    text-align: right; color: var(--ink);
    font-size: 11px; line-height: 15px; font-style: normal;
  }
  .contact .email { margin-top: 4px; }

  /* Back */
  .card-back {
    left: 629px;
    background: linear-gradient(180deg, var(--back-top) 0%, #7fb4e6 55%, var(--back-bottom) 100%);
  }
  .back-brand {
    position: absolute; left: 0; right: 0; top: 128px;
    display: flex; align-items: center; justify-content: center; gap: 16px;
  }
  .back-brand .brand-dot {
    width: 46px; height: 46px; border-radius: 50%;
    background: var(--brand-green);
  }
  .back-brand .brand-text { display: flex; flex-direction: column; }
  .back-brand .brand-name {
    font-weight: 700; font-size: 44px; line-height: 46px;
    color: var(--brand-green);
  }
  .back-brand .brand-tagline {
    font-weight: 700; font-size: 13px; letter-spacing: 1px;
    color: var(--brand-green); text-transform: uppercase; margin-top: 4px;
  }
</style>
</head>
<body>
<div class="canvas">
  <section class="card card-front">
    <div class="name-band"></div>
    <div class="front-brand">
      <span class="brand-dot"></span>
      <div class="brand-name">Brisk<br>Meadow</div>
      <div class="brand-tagline">Cooling and Yardcraft LLP</div>
    </div>
    <div class="names">
      <div>Dennis Holloway</div>
      <div>Mona Fairweather</div>
    </div>
    <address class="contact">
      <div>Phone: 340-555-0130</div>
      <div>Cell: 340-555-0147</div>
      <div>P.O. Box 618207</div>
      <div>Harbor Point, Port Laurel 04417</div>
      <div class="email">Briskmeadowcoolingandyardcraft@mailvessel.com</div>
    </address>
  </section>

  <section class="card card-back">
    <div class="back-brand">
      <span class="brand-dot"></span>
      <div class="brand-text">
        <div class="brand-name">Brisk Meadow</div>
        <div class="brand-tagline">Cooling and Yardcraft LLP</div>
      </div>
    </div>
  </section>
</div>
</body>
</html>
```